DOG DAYCARE BILLBOARD

Design a bold exciting billboard that can be read easily from a distance! Our goal is brand awareness and showcasing the services we offer (Boarding, Grooming, Daycare, and Training.
we would like to see examples with the phrase "your best friend's best day". Our name Bright Meadow Canine Activity Center (or just Bright Meadow might work better and could be bigger) and the services we provide.
(there are two examples of what we like included in the pictures)
you can find more information o our website at pawplayhub@mailnest.example.

```html
<!DOCTYPE html>
<html lang="en">
<head>
<meta charset="utf-8">
<title>Bright Meadow Billboard</title>
<link href="https://fonts.googleapis.com/css2?family=Montserrat:wght@600;700;800;900&family=Yellowtail&display=swap" rel="stylesheet">
<style>
  :root {
    --backdrop: #4f4f4f;
    --olive: #c6b800;
    --olive-dark: #ad9e00;
    --olive-shadow: #8f8300;
    --ink: #1d1d1b;
    --white: #ffffff;
    --pin: #c6b800;
    --dog-tan: #c98a4a;
    --dog-light: #e6c49a;
  }
  * { margin: 0; padding: 0; box-sizing: border-box; }
  html, body {
    width: 970px; height: 1200px; overflow: hidden;
    background: var(--backdrop);
    font-family: "Montserrat", Arial, sans-serif;
  }
  .billboard {
    position: absolute; left: 40px; top: 420px;
    width: 890px; height: 409px;
  }
  .billboard__field {
    position: absolute; left: 0; top: 0; width: 890px; height: 321px;
    background: linear-gradient(90deg, var(--olive) 0%, var(--olive) 80%, var(--olive-dark) 100%);
  }
  .billboard__field svg { position: absolute; inset: 0; }
  .billboard__footer {
    position: absolute; left: 0; top: 321px; width: 890px; height: 88px;
    background: var(--white);
  }
  .headline {
    position: absolute; left: 55px; top: 18px;
    color: var(--white); font-weight: 800; font-size: 54px;
    line-height: 52px; letter-spacing: -0.5px;
    text-shadow: 5px 4px 0 var(--olive-shadow);
  }
  .offer__lead {
    position: absolute; left: 20px; top: 210px;
    font-family: "Yellowtail", cursive; font-size: 30px; color: var(--ink);
    transform: rotate(-8deg);
  }
  .offer__list {
    position: absolute; left: 57px; top: 240px;
    font-weight: 700; font-size: 20px; color: var(--ink);
  }
  .offer__line {
    display: block; border-bottom: 1px solid var(--olive-shadow);
    padding-bottom: 4px; margin-bottom: 8px; width: max-content;
  }
  .offer__line--indent { padding-left: 36px; }
  .offer__and { font-size: 14px; font-weight: 700; }
  .dog-photo {
    position: absolute; left: 545px; top: -77px; width: 330px; height: 415px;
    border-radius: 60px 60px 20px 20px;
    background: radial-gradient(ellipse at 55% 55%, var(--dog-light) 0%, var(--dog-tan) 55%, rgba(201,138,74,0) 75%);
  }
  .brand-badge {
    position: absolute; left: 383px; top: 272px; width: 124px; height: 124px;
    border-radius: 50%; background: var(--white);
  }
  .brand-name {
    position: absolute; left: 375px; top: 350px; width: 140px;
    text-align: center; font-weight: 800; font-size: 17px; color: var(--ink);
  }
  .contact {
    position: absolute; font-weight: 700; color: var(--ink);
    display: flex; align-items: center; gap: 6px;
  }
  .contact svg { flex: none; }
  .contact--address { left: 52px; top: 345px; font-size: 12.5px; line-height: 18px; align-items: flex-start; }
  .contact--email { left: 606px; top: 347px; font-size: 11.5px; }
  .contact--phone { left: 606px; top: 367px; font-size: 17px; }
</style>
</head>
<body>
  <main class="billboard">
    <div class="billboard__field">
      <svg width="890" height="321" viewBox="0 0 890 321" aria-hidden="true">
        <polygon points="0,0 345,0 95,321 0,321" fill="var(--olive-dark)"/>
      </svg>
    </div>
    <div class="billboard__footer"></div>

    <div class="dog-photo" role="img" aria-label="Photo of a playful beagle in a play bow, tail raised"></div>

    <h1 class="headline">YOUR<br>BEST FRIEND'S<br>BEST DAY</h1>

    <p class="offer__lead">We offer</p>
    <p class="offer__list">
      <span class="offer__line">Boarding, Daycare, Grooming,</span>
      <span class="offer__line offer__line--indent"><span class="offer__and">and</span> Training</span>
    </p>

    <div class="brand-badge"></div>
    <p class="brand-name">Bright Meadow</p>

    <p class="contact contact--address">
      <svg width="12" height="16" viewBox="0 0 12 16"><path d="M6 1a5 5 0 0 0-5 5c0 4 5 9 5 9s5-5 5-9a5 5 0 0 0-5-5z" fill="none" stroke="var(--pin)" stroke-width="2"/></svg>
      <span>Bright Meadow, Canine Activity Center<br>480 W Orchard Ave. Maple Grove, IA 50000</span>
    </p>
    <p class="contact contact--email">
      <svg width="13" height="13" viewBox="0 0 13 13"><circle cx="6.5" cy="6.5" r="5.5" fill="none" stroke="var(--pin)" stroke-width="1.3"/><ellipse cx="6.5" cy="6.5" rx="2.5" ry="5.5" fill="none" stroke="var(--pin)" stroke-width="1"/><line x1="1" y1="6.5" x2="12" y2="6.5" stroke="var(--pin)" stroke-width="1"/></svg>
      <span>pawplayhub@mailnest.example</span>
    </p>
    <p class="contact contact--phone">
      <svg width="14" height="14" viewBox="0 0 14 14"><path d="M3 1l2.5 3-1.5 1.5c.8 1.8 2.2 3.2 4 4L9.5 8l3 2.5-1.5 2.5C6 13 1 8 1 2.5z" fill="var(--pin)"/></svg>
      <span>CALL NOW: (555) 014-2298</span>
    </p>
  </main>
</body>
</html>
```